Executive retreat/workshop flyer for Keystone Passage

Our company, Keystone Passage, runs intensive week long residential retreats for executives suffering from burnout syndrome. We have a programme of therapy which will enable clients to get clarity on what they want out of life and how to achieve it.

Our website is www.keystonepassage.example. The flyer should have a consistent look and feel to the website. The flyer should be suitable for electronic distribution as well as printing.

The copy should read:

What is it all for? (IN BIG BOLD FONT)

We invite you to The Keystone Passage

Discover a more meaningful way of being in this world and put passion and purpose back into your life.

Our leading experts will guide you through a holistic program of intellectual, physical, emotional, spiritual and financial work.

You will:

- Draw up a vision of how you want to live your life
- Understand negative behavior loops and how to manage them
- Rebalance relationships which have suffered from stress and neglect
- Examine your attitudes towards money through the Octavial System
- Access practical advice on how to implement your goals

Please join us in the beautiful Tarrowby Peninsula this August for a life-changing journey.

This is an intensive program custom tailored to your individual needs. We can only take on a very limited number of participants to maintain intimacy and quality of attention. Book early to avoid disappointment.

Details:

date - mon 27 August - sat 1 sept 2012

Venue- kestrelwood Eco retreat, stony vale, Australia, 1 hour from Melbourne

Price- Special launch offer of US$ 13,860 which is a 30% discount off the normal price of US$ 19,800

10% of profits go to charity

All accommodation, food and individual consultations included.

Please email info@keystonepassage.example or contact Marnie at 9316 2047

Target Market(s)

Senior executives and leaders mostly with a financial background.

Industry/Entity Type

Residential

Requirements
Must have
• The brochure should look clear in electronic and print format. Can use photos which I've attached.
Nice to have
• Should have a warm, serene feel but appear professional and reliable.

```html
<!DOCTYPE html>
<html lang="en">
<head>
<meta charset="utf-8">
<title>What is it all for? – The Keystone Passage</title>
<link rel="stylesheet" href="https://fonts.googleapis.com/css2?family=Archivo+Black&family=Arimo:wght@400;700&family=Sorts+Mill+Goudy&display=swap">
<style>
  :root {
    --backdrop: #e8e8e8;
    --paper: #ffffff;
    --plum: #5a0f55;
    --plum-deep: #4a0a47;
    --mauve: #8a4f8a;
    --sand: #ddd8bc;
    --cream: #efecdf;
    --olive: #7d7a1c;
    --white: #ffffff;
  }
  * { margin: 0; padding: 0; box-sizing: border-box; }
  html, body { width: 1200px; height: 900px; overflow: hidden; background: var(--backdrop); }
  .flyer {
    position: absolute; left: 300px; top: 22px; width: 597px; height: 844px;
    background: var(--paper); font-family: "Arimo", Arial, sans-serif;
  }
  .headline {
    position: absolute; left: 45px; top: 58px;
    font-family: "Archivo Black", "Arial Black", sans-serif;
    font-size: 41px; color: var(--plum); letter-spacing: -0.3px;
  }
  .feature {
    position: absolute; left: 0; top: 148px; width: 597px; height: 450px;
    background:
      radial-gradient(circle at 38% 42%, rgba(190,120,180,0.45), transparent 28%),
      radial-gradient(circle at 85% 20%, rgba(150,40,90,0.5), transparent 35%),
      radial-gradient(circle at 20% 80%, rgba(120,30,80,0.45), transparent 40%),
      linear-gradient(160deg, #5e1258 0%, var(--plum-deep) 60%, #571050 100%);
  }
  .timeline { position: absolute; left: 0; top: 0; }
  .section { position: absolute; left: 166px; width: 372px; color: var(--white); }
  .section-title { font-family: "Sorts Mill Goudy", Georgia, serif; font-size: 19px; }
  .lead { font-weight: 700; font-size: 12px; line-height: 14px; margin-top: 16px; }
  .body-copy { font-size: 8.4px; line-height: 13px; margin-top: 12px; }
  .intro { top: 30px; }
  .outcomes { top: 170px; }
  .outcomes ul { list-style: none; margin-top: 10px; }
  .outcomes li { display: flex; align-items: center; font-size: 8.4px; height: 22.3px; }
  .outcomes svg { margin: 0 14px 0 10px; flex: none; }
  .invitation { top: 336px; }
  .invitation .lead { margin-top: 0; }
  .invitation .body-copy { margin-top: 12px; }

  .detail { position: absolute; left: 0; width: 331px; text-align: center; color: var(--plum); }
  .detail-label { font-family: "Sorts Mill Goudy", Georgia, serif; font-size: 18px; line-height: 20px; }
  .detail-text { font-size: 8.4px; line-height: 11px; letter-spacing: 0.3px; }
  .detail-text strong { font-weight: 700; }
  .date { top: 598px; height: 53px; background: var(--mauve); color: var(--white); padding-top: 10px; }
  .date .detail-text { font-weight: 700; }
  .venue { top: 651px; height: 55px; background: var(--sand); padding-top: 7px; }
  .price { top: 706px; height: 55px; background: var(--cream); padding-top: 8px; }
  .notes { top: 770px; font-size: 8.4px; line-height: 24px; }
  .contact {
    position: absolute; left: 331px; top: 598px; width: 266px; height: 53px;
    background: var(--plum); color: var(--white); text-align: center;
    font-weight: 700; font-size: 12px; line-height: 20px; padding-top: 6px;
  }
  .brand { position: absolute; left: 331px; top: 700px; width: 266px; text-align: center; }
  .brand-mark { display: inline-block; width: 10px; height: 10px; border-radius: 50%; background: var(--plum); margin-bottom: 12px; }
  .brand-name { font-family: "Sorts Mill Goudy", Georgia, serif; font-size: 21px; color: var(--olive); letter-spacing: 0.5px; }
  .brand-url { font-family: "Sorts Mill Goudy", Georgia, serif; font-size: 16px; color: var(--plum); margin-top: 10px; }
</style>
</head>
<body>
<main class="flyer">
  <h1 class="headline">What is it all for?</h1>

  <section class="feature" role="img" aria-label="Soft-focus photograph of autumn leaves washed in deep purple">
    <svg class="timeline" width="597" height="450" aria-hidden="true">
      <g stroke="#ffffff" stroke-width="1" fill="#ffffff">
        <line x1="107" y1="42" x2="107" y2="450"/>
        <line x1="107" y1="42" x2="137" y2="42"/>
        <line x1="107" y1="183" x2="137" y2="183"/>
        <line x1="107" y1="344" x2="137" y2="344"/>
        <circle cx="137" cy="42" r="3.2"/>
        <circle cx="137" cy="183" r="3.2"/>
        <circle cx="137" cy="344" r="3.2"/>
      </g>
    </svg>

    <div class="section intro">
      <h2 class="section-title">We invite you to The Keystone Passage</h2>
      <p class="lead">Discover a more meaningful way of being in this world and put passion and purpose back into your life.</p>
      <p class="body-copy">Our leading experts will guide you through a holistic program of intellectual, physical, emotional, spiritual and financial work.</p>
    </div>

    <div class="section outcomes">
      <h2 class="section-title">You will:</h2>
      <ul>
        <li><svg width="13" height="12" viewBox="0 0 13 12"><path d="M1 11 C1 4 6 1 12 1 C12 7 8 11 1 11Z" fill="#fff"/></svg>Draw up a vision of how you want to live your life</li>
        <li><svg width="13" height="12" viewBox="0 0 13 12"><path d="M1 11 C1 4 6 1 12 1 C12 7 8 11 1 11Z" fill="#fff"/></svg>Understand negative behavior loops and how to manage them</li>
        <li><svg width="13" height="12" viewBox="0 0 13 12"><path d="M1 11 C1 4 6 1 12 1 C12 7 8 11 1 11Z" fill="#fff"/></svg>Rebalance relationships which have suffered from stress and neglect</li>
        <li><svg width="13" height="12" viewBox="0 0 13 12"><path d="M1 11 C1 4 6 1 12 1 C12 7 8 11 1 11Z" fill="#fff"/></svg>Examine your attitudes towards money through the Octavial System</li>
        <li><svg width="13" height="12" viewBox="0 0 13 12"><path d="M1 11 C1 4 6 1 12 1 C12 7 8 11 1 11Z" fill="#fff"/></svg>Access practical advice on how to implement your goals</li>
      </ul>
    </div>

    <div class="section invitation">
      <p class="lead">Please join us in the beautiful Tarrowby Peninsula this August for a life-changing journey.</p>
      <p class="body-copy">This is an intensive program custom tailored to your individual needs. We can only take on a very limited number of participants to maintain intimacy and quality of attention.<br>Book early to avoid disappointment.</p>
    </div>
  </section>

  <div class="detail date">
    <div class="detail-label">Date:</div>
    <div class="detail-text">Monday 27th August - Saturday 1st September 2012</div>
  </div>
  <div class="detail venue">
    <div class="detail-label">Venue:</div>
    <div class="detail-text"><strong>Kestrelwood Eco Retreat, Stony Vale, Australia,</strong><br>(1 hour from Melbourne)</div>
  </div>
  <div class="detail price">
    <div class="detail-label">Price:</div>
    <div class="detail-text"><strong>Special launch offer of US$ 13,860</strong><br>which is a 30% discount off the normal price of US$ 19,800</div>
  </div>
  <div class="detail notes">
    <p>10% of profits go to charity</p>
    <p>All accommodation, food and individual consultations included.</p>
  </div>

  <div class="contact">
    <p>Please email: info@keystonepassage.example</p>
    <p>or contact Marnie at 9316 2047</p>
  </div>

  <div class="brand">
    <span class="brand-mark"></span>
    <div class="brand-name">The Keystone Passage</div>
    <div class="brand-url">www.keystonepassage.example</div>
  </div>
</main>
</body>
</html>
```